Redesign My Travel Voucher Coupons-Please redesign the flyers I have attached to this brief.

These designs will be catered towards like travel agency vacation stays...luxury resort stays, hotel and airfare getaways, etc. so must have a travel theme but more importantly professional trustworthy appeal...

Please redesign the flyers I have attached to this brief.

I have attached my existing designs. Please use all existing content and elements exactly but make the design much better...also, please keep in mind that these would be full color and printer friendly...

Target Market(s)

Consumers. People receive these vouchers from businesses that run marketing promotions and contests and giveaways. So the look and feel must feel professional and trustworthy but not cheesy and fake.

Industry/Entity Type

Hotel

Requirements
Must have
• Please use all existing content and elements exactly but make the design much better...also, please keep in mind that these would be full color and printer friendly...

MUST HAVE ALL EXISTING CONTENT EXACT NO EXCEPTIONS
Nice to have
• These designs will be catered towards like travel agency vacation stays...luxury resort stays, hotel and airfare getaways, etc. so must have a travel theme but more importantly professional trustworthy appeal...

Should not have

```html
<!DOCTYPE html>
<html lang="en">
<head>
<meta charset="utf-8">
<title>Travel Voucher – $500 Off</title>
<link href="https://fonts.googleapis.com/css2?family=Archivo:wght@700;800;900&family=Bebas+Neue&family=Roboto:wght@400;500;700&display=swap" rel="stylesheet">
<style>
  :root{
    --red:#c8202b;
    --red-light:#ec4a52;
    --ink:#2b2b2e;
    --body:#3a3a3d;
    --muted:#6d6d72;
    --silver:#9a9aa0;
    --paper:#f4f4f5;
    --paper-edge:#dcdcde;
    --stage:#000;
  }
  *{box-sizing:border-box;margin:0;padding:0}
  html,body{width:974px;height:1200px;overflow:hidden;background:var(--stage)}
  .flyer{position:absolute;left:92px;top:89px;width:790px;height:1022px;overflow:hidden;
    background:radial-gradient(ellipse at 50% 65%,#fbfbfb 0%,var(--paper) 55%,var(--paper-edge) 100%);
    font-family:"Roboto",sans-serif;color:var(--body)}
  .hero{position:absolute;left:0;top:0;width:790px;height:480px}
  .abs{position:absolute}
  .headline-enjoy{left:26px;top:14px;font-family:"Bebas Neue",sans-serif;font-size:140px;line-height:1;
    color:var(--red);letter-spacing:-1px;
    background:linear-gradient(180deg,#b3121b 0%,var(--red) 50%,var(--red-light) 100%);
    -webkit-background-clip:text;background-clip:text;-webkit-text-fill-color:transparent}
  .offer-band{left:28px;top:128px;width:296px;height:49px;
    background:linear-gradient(90deg,#b8141c,var(--red) 60%,var(--red-light));
    clip-path:polygon(0 0,84% 0,100% 100%,0 100%);
    font-family:"Archivo",sans-serif;font-weight:900;font-size:43px;line-height:49px;color:#fff;padding-left:13px}
  .offer-line{left:28px;top:180px;font-family:"Archivo",sans-serif;font-weight:800;font-size:25px;color:var(--red);white-space:nowrap}
  .offer-sub{left:29px;top:211px;font-family:"Archivo",sans-serif;font-weight:800;font-size:18.5px;color:var(--ink);white-space:nowrap}
  .sponsor-card{left:598px;top:1px;width:157px;height:120px;background:#fff;text-align:center;padding-top:26px}
  .sponsor-card .compliments{font-weight:700;font-size:9.5px;color:var(--red)}
  .sponsor-card .brand{margin-top:9px;display:flex;align-items:center;justify-content:center;gap:4px;
    font-weight:700;font-size:10px;color:var(--red)}
  .sponsor-card .brand-dot{width:9px;height:9px;border-radius:50%;background:var(--red)}
  .sponsor-card .rep{margin-top:10px;font-size:11.5px;color:var(--ink);line-height:14px}
  .sponsor-card .site{font-size:9px;color:var(--ink);margin-top:1px}
  .photo-ring{position:absolute;border-radius:50%;padding:7px;
    background:linear-gradient(135deg,#f2f2f3,#8e8e94 45%,#e6e6e8 70%,#7c7c82);
    box-shadow:0 2px 6px rgba(0,0,0,.25)}
  .photo-ring .photo{width:100%;height:100%;border-radius:50%}
  .ring-savings{left:470px;top:290px;width:196px;height:196px}
  .ring-savings .photo{background:radial-gradient(circle at 60% 60%,#e9b7a6,#b6a46a 45%,#6f8d3b 80%)}
  .ring-beach{left:429px;top:478px;width:152px;height:152px}
  .ring-beach .photo{background:linear-gradient(180deg,#5fb6ea 0%,#a9ddf5 55%,#f1e6d0 75%,#e9c9d5 100%)}
  .ring-cash{left:584px;top:461px;width:168px;height:168px}
  .ring-cash .photo{background:radial-gradient(circle at 55% 45%,#e64a4a,#c8a88c 55%,#c49a6a 100%)}
  .section-tag{position:absolute;height:24px;padding-left:10px;
    background:linear-gradient(90deg,#b8141c,var(--red) 60%,var(--red-light));
    clip-path:polygon(0 0,84% 0,100% 100%,0 100%);
    font-family:"Bebas Neue",sans-serif;font-size:21px;line-height:26px;color:#fff;letter-spacing:.2px}
  .tag-exclusive{left:28px;top:486px;width:160px}
  .tag-features{left:28px;top:621px;width:160px}
  .tag-how{left:375px;top:659px;width:183px}
  .tag-reviews{left:375px;top:781px;width:158px}
  .copy{position:absolute;font-size:10px;line-height:12.2px;color:var(--body);text-align:justify}
  .copy-exclusive{left:38px;top:516px;width:306px}
  .copy-how{left:384px;top:690px;width:382px;line-height:13.6px;text-align:left}
  .column-rule{left:361px;top:486px;width:1px;height:399px;background:var(--silver)}
  .feature-list{position:absolute;left:32px;top:650px;width:320px;display:grid;
    grid-template-columns:176px 144px;grid-auto-rows:47px;row-gap:1px}
  .feature{display:flex;align-items:center;gap:9px;font-size:12px;line-height:15.5px;color:var(--ink)}
  .feature svg{flex:none;width:32px;height:32px;stroke:#6a6a6f;fill:none;stroke-width:1.6;stroke-linecap:round;stroke-linejoin:round}
  .testimonial{left:375px;top:812px;width:385px;font-size:10px;line-height:13.7px;color:var(--body)}
  .testimonial p{padding-left:21px;position:relative}
  .quote-mark{font-family:"Archivo",sans-serif;font-weight:900;font-size:26px;color:#6d6d72;line-height:1}
  .quote-open{position:absolute;left:0;top:-3px}
  .quote-close{position:relative;top:9px;margin-left:4px}
  .reviewer{text-align:right;margin-top:10px;padding-right:20px;font-size:10.5px;color:var(--ink)}
  .coupon{left:29px;top:902px;width:732px;height:92px;border:2px dashed var(--red);border-radius:12px}
  .coupon-id{position:absolute;left:0;top:0;width:181px;height:100%;border-right:2px dashed var(--red);text-align:center}
  .coupon-id .label{font-size:11px;color:var(--ink)}
  .coupon-id .value{font-size:17px;color:var(--red);line-height:19px}
  .coupon-id .id-block{padding-top:12px;padding-bottom:6px;margin:0 34px;border-bottom:1px solid var(--silver)}
  .coupon-id .exp-block{padding-top:5px}
  .coupon-redeem{position:absolute;left:181px;right:0;top:0;text-align:center;padding-top:9px}
  .coupon-redeem .lead{font-size:14px;line-height:17px;color:var(--ink);font-weight:500}
  .coupon-redeem .url{margin-top:3px;font-size:20px;letter-spacing:3.6px;color:var(--red);font-weight:500}
  .coupon-redeem .terms{font-size:8px;color:var(--ink);margin-top:1px}
</style>
</head>
<body>
<main class="flyer">
  <svg class="hero" viewBox="0 0 790 480" aria-hidden="false">
    <defs>
      <linearGradient id="heroTone" x1="0" y1="1" x2="1" y2="0">
        <stop offset="0" stop-color="#6f7494"/>
        <stop offset=".45" stop-color="#c3c4d6"/>
        <stop offset=".8" stop-color="#e3c6c8"/>
        <stop offset="1" stop-color="#e6b7b4"/>
      </linearGradient>
    </defs>
    <path role="img" aria-label="Traveller walking past airport terminal windows with a plane taking off" fill="url(#heroTone)"
      d="M0 0H790V405C745 398 705 335 645 293C595 262 530 268 490 318C420 408 330 468 200 468C110 468 40 420 0 377Z"/>
    <path fill="none" stroke="#8b8b91" stroke-width="7"
      d="M790 409C745 402 705 339 645 297C595 266 530 272 490 322C420 412 330 472 200 472C110 472 40 424 0 381"/>
    <path fill="none" stroke="#d6d6d9" stroke-width="2"
      d="M790 414C745 407 705 344 645 302C595 271 530 277 490 327C420 417 330 477 200 477C110 477 40 429 0 386"/>
  </svg>

  <div class="abs headline-enjoy">ENJOY</div>
  <div class="abs offer-band">$500 OFF</div>
  <div class="abs offer-line">Get $500 Off At Over 400,000</div>
  <div class="abs offer-sub">Hotel &amp; Resort Properties Worldwide!</div>

  <aside class="abs sponsor-card">
    <div class="compliments">Compliments Of</div>
    <div class="brand"><span class="brand-dot"></span>Brightpath Promotions</div>
    <div class="rep">Dana Whitfield<br>555-014-2290</div>
    <div class="site">www.ReachMoreGuests.com</div>
  </aside>

  <div class="photo-ring ring-savings"><div class="photo" role="img" aria-label="Coins stacked beside a toy plane and a pink suitcase"></div></div>
  <div class="photo-ring ring-beach"><div class="photo" role="img" aria-label="Piggy bank in sunglasses on a tropical beach"></div></div>
  <div class="photo-ring ring-cash"><div class="photo" role="img" aria-label="Dollar bills on a beach chair under a red umbrella"></div></div>

  <h2 class="section-tag tag-exclusive">EXCLUSIVELY FOR:</h2>
  <p class="copy copy-exclusive">The best discounts available in travel. Web-based technologies focused on having the absolute lowest prices on hotels, resorts and other travel products. Proprietary technology has created an all-encompassing, easy-to-use web platform that brings unparalleled pricing to all types of travelers. Superior customer service and online transparency allows for credibility and consistency to customers and site users, making it the fastest growing travel website aggregator.</p>

  <h2 class="section-tag tag-features">FEATURES</h2>
  <ul class="feature-list">
    <li class="feature"><svg viewBox="0 0 32 32"><path d="M4 3h24M8 3v4M24 3v4"/><rect x="5" y="9" width="22" height="20"/><path d="M9 22l1 1M16 22l1 1M23 22l1 1"/></svg>400,000 Top Brand<br>Hotels &amp; Resorts</li>
    <li class="feature"><svg viewBox="0 0 32 32"><rect x="3" y="5" width="26" height="24" rx="2"/><path d="M3 11h26M9 2v6M23 2v6"/><circle cx="12" cy="17" r="2"/><circle cx="19" cy="17" r="2"/><circle cx="12" cy="24" r="2"/><circle cx="19" cy="24" r="2"/></svg>12 Months To<br>Book Travel</li>
    <li class="feature"><svg viewBox="0 0 32 32"><path d="M3 12a13 9 0 0 1 26 0z"/><path d="M16 12v4"/><rect x="7" y="16" width="18" height="13" rx="2"/><path d="M12 23l8-4"/></svg>Redeem Now,<br>Travel Later</li>
    <li class="feature"><svg viewBox="0 0 32 32"><path d="M4 22l8-16 4 6 10 4c2 1 2 4 0 5l-5 2H6z"/><path d="M10 25l-2 4"/></svg>Thousands Of<br>Activities</li>
    <li class="feature"><svg viewBox="0 0 32 32"><circle cx="10" cy="7" r="4"/><path d="M5 20a11 8 0 0 1 22 0v2a11 8 0 0 1-22 0z"/><path d="M3 18h3M11 28v2M21 28v2"/></svg>Save Up To 50%<br>On Travel</li>
    <li class="feature"><svg viewBox="0 0 32 32"><rect x="4" y="5" width="24" height="18"/><path d="M2 27h28M16 8v12M10 15l6-3 6 3"/></svg>Easy Online<br>Bookings</li>
    <li class="feature"><svg viewBox="0 0 32 32"><rect x="5" y="5" width="22" height="24" rx="1"/><path d="M5 10h22M10 2v6M22 2v6"/><circle cx="16" cy="19" r="4"/><path d="M14 19h4"/></svg>No Blackout Dates<br>Or Restrictions</li>
    <li class="feature"><svg viewBox="0 0 32 32"><rect x="10" y="2" width="16" height="6"/><path d="M6 18l3-6h16l3 6v7H6z"/><circle cx="11" cy="25" r="2"/><circle cx="23" cy="25" r="2"/><circle cx="3" cy="19" r="2"/></svg>8,000 Rental Car<br>Locations</li>
    <li class="feature"><svg viewBox="0 0 32 32"><circle cx="9" cy="18" r="6"/><circle cx="23" cy="14" r="6"/><path d="M5 6h18l-3-3M27 26H9l3 3"/></svg>Fully Transferable<br>To Another Person</li>
    <li class="feature"><svg viewBox="0 0 32 32"><path d="M5 18l3-6h16l3 6v7H5z"/><circle cx="10" cy="22" r="2"/><circle cx="22" cy="22" r="2"/><path d="M9 12l2-5h10l2 5"/><path d="M8 5l2 2M24 5l-2 2M16 3v3"/></svg>Millions Of Happy<br>Travelers</li>
  </ul>

  <div class="abs column-rule"></div>

  <h2 class="section-tag tag-how">HOW CAN WE DO THIS?</h2>
  <p class="copy copy-how">Redeem your certificate to activate your account. Once activated you can login to your personal travel booking portal anytime you wish to check travel availability and book travel. Anytime you book travel you can use your travel dollars towards the booking to get your instant discount. It really is that easy!</p>

  <h2 class="section-tag tag-reviews">WHAT OTHERS SAY</h2>
  <blockquote class="abs testimonial">
    <p><span class="quote-mark quote-open">“</span>I saved a lot of money using my savings dollars. I get $100 every month for paying my insurance policy on time. I recently booked a 10 day vacation for Hawaii in 2021 and I saved over $1200!<span class="quote-mark quote-close">”</span></p>
    <footer class="reviewer">Tessa R. Kansas City, MO</footer>
  </blockquote>

  <section class="abs coupon">
    <div class="coupon-id">
      <div class="id-block"><div class="label">Certificate ID</div><div class="value">107083-11264</div></div>
      <div class="exp-block"><div class="label">Expires</div><div class="value">11/07/2020</div></div>
    </div>
    <div class="coupon-redeem">
      <div class="lead">VIEW ALL THE DETAILS OF THIS SPECIAL OFFER<br>AND REDEEM ONLINE AT</div>
      <div class="url">WWW.TRAVELPERKCENTER.COM</div>
      <div class="terms">*Terms and Conditions apply see website for details</div>
    </div>
  </section>
</main>
</body>
</html>
```